Vantage Systemworks Brochure

We are looking to design a trifold sales brochure for a building automation company. We focus on selling and installing Quorvex open protocol building management systems. We would like to design this around our black and red color scheme. Our company is based in Belmont Michigan just outside of Grand Rapids. Our Customer base is strictly commercial and industrial buildings no residential. Attached is a powerpoint with more of our company information.

```html
<!DOCTYPE html>
<html lang="en">
<head>
<meta charset="utf-8">
<title>Vantage Systemworks Brochure</title>
<link href="https://fonts.googleapis.com/css2?family=Kumbh+Sans:wght@400;500;700;800&display=swap" rel="stylesheet">
<style>
:root{
  --red:#e8383f;
  --dark:#222222;
  --ink:#222;
  --grey-band:#eeeeee;
  --muted:#8a8a8a;
  --white:#fff;
}
*{margin:0;padding:0;box-sizing:border-box}
html,body{width:1200px;height:849px;overflow:hidden;background:#fff}
body{font-family:"Kumbh Sans",sans-serif;color:var(--ink);position:relative}
.panel{position:absolute;top:0;height:849px;width:400px;overflow:hidden}
.panel-left{left:0;background:#fff}
.panel-mid{left:397px;width:403px;background:var(--dark);color:#fff}
.panel-right{left:800px;background:#fff}
.band{position:absolute;left:0;right:0;background:var(--grey-band)}
.abs{position:absolute}
.heading{position:absolute;left:31px;color:var(--red);font-weight:800;font-size:16.5px;line-height:18.5px;letter-spacing:.2px;text-transform:uppercase}
.rule{position:absolute;left:31px;width:228px;height:1.5px;background:var(--ink)}
.panel-mid .rule{background:#fff}
.rule::after{content:"";position:absolute;left:21px;top:-1px;width:42px;height:4px;background:var(--red)}
.body-text{position:absolute;left:31px;font-size:14.2px;line-height:17.2px}
.bullets{position:absolute;list-style:none;font-size:14.2px;line-height:21.6px}
.bullets li{position:relative;padding-left:14px}
.bullets li::before{content:"";position:absolute;left:0;top:7.5px;width:7px;height:7px;border-radius:50%;background:var(--red)}
.bullets .sub{color:var(--muted);padding-left:31px}
.bullets .sub::before{left:17px;background:#111}
.placeholder{position:absolute}
.promo{position:absolute;left:0;top:192px;width:330px;height:121px;background:var(--red)}
.promo-title{position:absolute;left:20px;top:207px;font-weight:800;font-size:16.5px;line-height:18.5px;color:#fff}
.caption{position:absolute;left:256px;top:322px;font-weight:700;font-size:10.6px;color:#fff;letter-spacing:.1px}
.benefit{position:absolute;left:23px;width:370px}
.benefit .icon{position:absolute;left:0;top:0;width:44px;height:44px}
.benefit h3{position:absolute;left:56px;top:-6px;color:var(--red);font-weight:500;font-size:15.3px;white-space:nowrap}
.benefit p{position:absolute;left:56px;top:14px;font-size:11.8px;line-height:17px;width:310px}
.brand-tag{position:absolute;left:1048px;top:243px;color:#5b87c7;font-size:11px;font-weight:500}
</style>
</head>
<body>

<!-- LEFT PANEL -->
<section class="panel panel-left">
  <div class="band" style="top:335px;height:261px"></div>

  <h2 class="heading" style="top:37px">System Architecture</h2>
  <div class="rule" style="top:58px"></div>
  <p class="body-text" style="top:69px;width:345px">Vantage Systemworks is a division of Halvorsen Mechanical, West Michigan's largest full service mechanical contractors for over 40 years. We focus on building long term relationships with our customers by providing a next level building automation experience. Our fulltime team of engineers and electricians are trained on mechanical and controls systems to make sure your building management system is performing at its full potential.</p>
  <p class="body-text" style="top:246px;width:180px">Our focus is growth through commitment to service and sustainability.</p>
  <div class="placeholder" role="img" aria-label="Illustration of two people reviewing a building plan in front of a house" style="left:210px;top:232px;width:168px;height:103px;background:linear-gradient(135deg,#e7eef4,#d9c9a0 60%,#9aa6b2);border-radius:6px"></div>

  <h2 class="heading" style="top:343px">What does<br>Vantage Systemworks offer?</h2>
  <div class="rule" style="top:387px"></div>
  <div class="placeholder" role="img" aria-label="Building floor plan with door access status labels" style="left:95px;top:403px;width:215px;height:177px;background:linear-gradient(180deg,#f6f6f6,#e2e4e8);border:1px solid #cfd3d8"></div>

  <h2 class="heading" style="top:606px">Services we offer</h2>
  <div class="rule" style="top:631px"></div>
  <div class="abs" style="left:31px;top:647px;font-size:14.5px;font-weight:800">BUILDING <span style="color:var(--red)">AUTOMATION</span></div>
  <ul class="bullets" style="left:31px;top:669px">
    <li>Quorvex Base Building Automation Systems</li>
    <li>Open Unitary Controllers</li>
    <li>HVAC &amp; Process Controls</li>
    <li>Lighting Control</li>
    <li>Card Access</li>
    <li>Commercial &amp; Industrial Installation<br>with 24/7 Service</li>
  </ul>
</section>

<!-- MIDDLE PANEL -->
<section class="panel panel-mid">
  <h2 class="heading" style="left:24px;top:37px">Electrical</h2>
  <ul class="bullets" style="left:24px;top:56px;line-height:21.7px;font-size:14.5px">
    <li>Generator Installations</li>
    <li>Lighting Upgrades</li>
    <li>Service Upgrades</li>
    <li>Variable Frequency Drives</li>
    <li style="line-height:16.5px;margin-top:3px">Commercial and Industrial Installation<br>with 24/7 Service</li>
  </ul>

  <div class="promo"></div>
  <div class="placeholder" role="img" aria-label="Illustration of a concerned customer beside a house and apartment building" style="left:222px;top:188px;width:173px;height:125px;background:linear-gradient(160deg,#a9d2e6,#8fc0da 55%,#f2c75c);border-radius:60px 70px 10px 60px"></div>
  <h2 class="promo-title">WHAT IS THE BENEFIT<br>OF AN OPEN<br>PROTOCOL SYSTEM<br>OVER A PROPRIETARY<br>SYSTEM?</h2>
  <div class="caption">CONCERNED CUSTOMER</div>

  <h2 class="heading" style="left:24px;top:360px">Benefits of<br>an open system</h2>
  <div class="rule" style="left:24px;top:401px"></div>

  <div class="benefit" style="top:420px">
    <svg class="icon" viewBox="0 0 44 44"><circle cx="22" cy="22" r="22" fill="#e8383f"/><g fill="none" stroke="#fff" stroke-width="2"><circle cx="22" cy="17" r="5"/><path d="M13 31c1-5 5-8 9-8s8 3 9 8"/><circle cx="12" cy="20" r="3"/><circle cx="32" cy="20" r="3"/></g></svg>
    <h3>Interoperability</h3>
    <p>Devices and systems from different manufacturers to communicate and work together.</p>
  </div>
  <div class="benefit" style="top:490px">
    <svg class="icon" viewBox="0 0 44 44"><circle cx="22" cy="22" r="22" fill="#e8383f"/><g fill="none" stroke="#fff" stroke-width="2"><path d="M14 16h16l2 17H12z"/><path d="M18 16c0-6 8-6 8 0"/></g></svg>
    <h3>Vendor Neutrality</h3>
    <p>You're not tied to a single vendor for all your components.</p>
  </div>
  <div class="benefit" style="top:557px">
    <svg class="icon" viewBox="0 0 44 44"><circle cx="22" cy="22" r="22" fill="#e8383f"/><g stroke="#fff" stroke-width="2" fill="#fff"><line x1="22" y1="22" x2="22" y2="11"/><line x1="22" y1="22" x2="12" y2="17"/><line x1="22" y1="22" x2="32" y2="17"/><line x1="22" y1="22" x2="14" y2="31"/><line x1="22" y1="22" x2="30" y2="31"/><circle cx="22" cy="22" r="3.5"/><circle cx="22" cy="11" r="2.5"/><circle cx="12" cy="17" r="2.5"/><circle cx="32" cy="17" r="2.5"/><circle cx="14" cy="31" r="2.5"/><circle cx="30" cy="31" r="2.5"/></g></svg>
    <h3>Scalability</h3>
    <p>More adaptable to changes in building size or functionality.</p>
  </div>
  <div class="benefit" style="top:629px">
    <svg class="icon" viewBox="0 0 44 44"><circle cx="22" cy="22" r="22" fill="#e8383f"/><g fill="none" stroke="#fff" stroke-width="2" stroke-linecap="round"><path d="M22 34V24c0-4-4-7-9-9"/><path d="M22 24c0-4 4-7 9-9"/><path d="M11 12l2 3-3 2"/><path d="M33 12l-2 3 3 2"/></g></svg>
    <h3>Flexibility</h3>
    <p>Allows for more customization and fine-tuning of system behavior.</p>
  </div>
  <div class="benefit" style="top:698px">
    <svg class="icon" viewBox="0 0 44 44"><circle cx="22" cy="22" r="22" fill="#e8383f"/><g fill="none" stroke="#fff" stroke-width="2"><rect x="14" y="13" width="15" height="20" rx="1"/><rect x="18" y="11" width="7" height="4"/><line x1="17" y1="21" x2="25" y2="21"/><line x1="17" y1="25" x2="23" y2="25"/><path d="M27 29l6-9"/></g></svg>
    <h3>Ease of Integration</h3>
    <p>Easier to integrate with other building systems, such as lighting and security.</p>
  </div>
  <div class="benefit" style="top:770px">
    <svg class="icon" viewBox="0 0 44 44"><circle cx="22" cy="22" r="22" fill="#e8383f"/><g fill="none" stroke="#fff" stroke-width="2"><rect x="10" y="18" width="24" height="12" rx="1"/><circle cx="22" cy="24" r="2.5"/><path d="M13 18l16-5 2 5"/></g></svg>
    <h3>Reduced Costs</h3>
    <p>The competition among vendors and the ability to mix and match components can lead to cost savings.</p>
  </div>
</section>

<!-- RIGHT PANEL -->
<section class="panel panel-right">
  <div class="band" style="top:275px;height:260px"></div>

  <h2 class="heading" style="left:18px;top:37px">System Architecture</h2>
  <div class="rule" style="left:18px;top:58px"></div>
  <div class="placeholder" role="img" aria-label="Network architecture diagram of supervisors, controllers and field devices" style="left:90px;top:72px;width:205px;height:165px;background:linear-gradient(180deg,#f4f7fb,#dfe8f3);border-radius:4px"></div>
  <div class="abs" style="left:248px;top:243px;color:#5b87c7;font-size:11px;font-weight:500">lumora</div>

  <h2 class="heading" style="left:18px;top:287px">Alarm Console</h2>
  <div class="rule" style="left:18px;top:309px"></div>
  <div class="placeholder" role="img" aria-label="Alarm console dashboard showing critical, general and total alarm counts" style="left:15px;top:330px;width:362px;height:173px;background:linear-gradient(180deg,#1f3d8a 0,#2b5fb8 28px,#ffffff 28px,#f7f8fa);border:1px solid #d5d9e0"></div>

  <h2 class="heading" style="left:18px;top:551px">Schedules</h2>
  <div class="rule" style="left:18px;top:573px"></div>
  <div class="placeholder" role="img" aria-label="Line sketch of a multi-storey commercial building" style="left:160px;top:720px;width:240px;height:129px;background:linear-gradient(135deg,rgba(255,255,255,0),rgba(200,200,200,.35));"></div>
  <ul class="bullets" style="left:18px;top:586px;line-height:21.2px">
    <li>KPS HS-Access Right Schedules</li>
    <li>KPS HS-HVAC Schedules</li>
    <li>KPS HS-Access C Schedules</li>
    <li>KPS MS HVAC Schedules</li>
    <li>KPS Alderwood – HVAC Schedules</li>
    <li>Currently False</li>
    <li class="sub">District Calendar Schedule</li>
    <li class="sub">Occupy Building Schedule</li>
    <li class="sub">Calendar Schedule</li>
    <li class="sub">Holidays</li>
  </ul>
</section>

</body>
</html>
```